Pillar Orchard
Professional
Mira Castellan, MBA
mira@pillarorchard.ca
www.pillarorchard.ca
Landscape layout. Please include tagline: "Building Momentum for Success"
Whatever you think will look good.

```html
<!DOCTYPE html>
<html lang="en">
<head>
<meta charset="utf-8">
<title>Pillar Orchard – Business Cards</title>
<link href="https://fonts.googleapis.com/css2?family=Open+Sans:wght@400;600;700&display=swap" rel="stylesheet">
<style>
  :root {
    --page-bg: #e9e6e1;
    --card-black: #0b0b0d;
    --card-black-soft: #25262a;
    --card-white: #ffffff;
    --brand-blue: #1d3a8f;
    --brand-blue-deep: #0f1f5c;
    --brand-blue-light: #3c5fc4;
    --swoosh-grey: #b9bcc2;
    --swoosh-grey-dark: #6d7079;
    --text-light: #ffffff;
    --text-muted-light: #c9cbd2;
    --text-muted-dark: #5b6070;
    --logo-dark: #1b2f78;
  }
  * { margin: 0; padding: 0; box-sizing: border-box; }
  html, body { width: 1200px; height: 852px; overflow: hidden; }
  body {
    background: var(--page-bg);
    font-family: "Open Sans", Arial, sans-serif;
    position: relative;
  }
  .card {
    position: absolute;
    width: 560px;
    height: 320px;
    border-radius: 18px;
    overflow: hidden;
    box-shadow: 0 6px 18px rgba(0,0,0,0.18);
  }
  .card--dark { left: 110px; top: 70px; background: linear-gradient(160deg, var(--card-black-soft), var(--card-black) 60%); }
  .card--light { left: 530px; top: 462px; background: var(--card-white); }
  .card__swoosh { position: absolute; inset: 0; width: 100%; height: 100%; }

  .brand {
    position: absolute;
    width: 200px;
    display: flex;
    flex-direction: column;
    align-items: center;
    gap: 10px;
  }
  .card--dark .brand { left: 40px; top: 34px; }
  .card--light .brand { left: 20px; top: 50px; }
  .brand__mark {
    width: 70px; height: 70px; border-radius: 50%;
    background: var(--brand-blue);
  }
  .brand__name {
    font-weight: 700;
    font-size: 30px;
    line-height: 1.05;
    letter-spacing: 2px;
    text-align: center;
    text-transform: uppercase;
  }
  .brand__tagline {
    font-size: 10px;
    font-weight: 600;
    letter-spacing: 0.3px;
    text-align: center;
    white-space: nowrap;
  }
  .card--dark .brand__name { color: var(--text-light); }
  .card--dark .brand__tagline { color: var(--text-muted-light); }
  .card--light .brand__name { color: var(--logo-dark); }
  .card--light .brand__tagline { color: var(--text-muted-dark); }

  .contact {
    position: absolute;
    right: 34px;
    color: var(--text-light);
    text-align: right;
  }
  .card--dark .contact { top: 148px; }
  .card--light .contact { top: 160px; }
  .contact__name { font-size: 19px; font-weight: 700; margin-bottom: 30px; white-space: nowrap; }
  .contact__line {
    font-size: 13px;
    display: flex;
    justify-content: flex-end;
    align-items: center;
    gap: 10px;
    margin-bottom: 6px;
  }
  .contact__line--web { padding-right: 24px; }
  .contact__icon { width: 14px; height: 14px; fill: var(--text-light); }
</style>
</head>
<body>

<article class="card card--dark">
  <svg class="card__swoosh" viewBox="0 0 560 320" preserveAspectRatio="none" aria-hidden="true">
    <defs>
      <linearGradient id="blueDark" x1="0" y1="1" x2="1" y2="0">
        <stop offset="0" stop-color="var(--brand-blue-deep)"/>
        <stop offset="0.55" stop-color="var(--brand-blue)"/>
        <stop offset="1" stop-color="var(--brand-blue-light)"/>
      </linearGradient>
    </defs>
    <path d="M0,250 C140,290 250,230 320,150 C390,70 470,20 560,10 L560,40 C470,50 400,100 335,170 C265,250 150,300 0,275 Z" fill="var(--swoosh-grey-dark)"/>
    <path d="M0,270 C150,300 262,245 332,168 C402,92 475,45 560,34 L560,320 L0,320 Z" fill="url(#blueDark)"/>
  </svg>
  <div class="brand">
    <span class="brand__mark"></span>
    <span class="brand__name">Pillar<br>Orchard</span>
    <span class="brand__tagline">Building Momentum for Success</span>
  </div>
  <div class="contact">
    <p class="contact__name">Mira Castellan, MBA</p>
    <p class="contact__line">604-555-0187
      <svg class="contact__icon" viewBox="0 0 24 24"><path d="M6.6 10.8a15.1 15.1 0 0 0 6.6 6.6l2.2-2.2a1 1 0 0 1 1-.25 11.4 11.4 0 0 0 3.6.57 1 1 0 0 1 1 1V20a1 1 0 0 1-1 1A17 17 0 0 1 3 4a1 1 0 0 1 1-1h3.5a1 1 0 0 1 1 1c0 1.25.2 2.45.57 3.6a1 1 0 0 1-.25 1z"/></svg>
    </p>
    <p class="contact__line">mira@pillarorchard.ca
      <svg class="contact__icon" viewBox="0 0 24 24"><path d="M2 5h20v14H2z M4 7v.5l8 5 8-5V7z" fill-rule="evenodd"/></svg>
    </p>
    <p class="contact__line contact__line--web">www.pillarorchard.ca</p>
  </div>
</article>

<article class="card card--light">
  <svg class="card__swoosh" viewBox="0 0 560 320" preserveAspectRatio="none" aria-hidden="true">
    <defs>
      <linearGradient id="blueLight" x1="0" y1="1" x2="1" y2="0">
        <stop offset="0" stop-color="var(--brand-blue-deep)"/>
        <stop offset="0.5" stop-color="var(--brand-blue)"/>
        <stop offset="1" stop-color="var(--brand-blue-light)"/>
      </linearGradient>
    </defs>
    <path d="M0,320 C160,300 230,230 280,152 C335,72 450,25 560,18 L560,48 C460,58 360,95 300,170 C240,250 180,312 50,320 Z" fill="var(--swoosh-grey)"/>
    <path d="M50,320 C180,312 240,250 300,170 C360,95 460,58 560,46 L560,320 Z" fill="url(#blueLight)"/>
  </svg>
  <div class="brand">
    <span class="brand__mark"></span>
    <span class="brand__name">Pillar<br>Orchard</span>
    <span class="brand__tagline">Building Momentum for Success</span>
  </div>
  <div class="contact">
    <p class="contact__name">Mira Castellan, MBA</p>
    <p class="contact__line">604-555-0187
      <svg class="contact__icon" viewBox="0 0 24 24"><path d="M6.6 10.8a15.1 15.1 0 0 0 6.6 6.6l2.2-2.2a1 1 0 0 1 1-.25 11.4 11.4 0 0 0 3.6.57 1 1 0 0 1 1 1V20a1 1 0 0 1-1 1A17 17 0 0 1 3 4a1 1 0 0 1 1-1h3.5a1 1 0 0 1 1 1c0 1.25.2 2.45.57 3.6a1 1 0 0 1-.25 1z"/></svg>
    </p>
    <p class="contact__line">mira@pillarorchard.ca
      <svg class="contact__icon" viewBox="0 0 24 24"><path d="M2 5h20v14H2z M4 7v.5l8 5 8-5V7z" fill-rule="evenodd"/></svg>
    </p>
    <p class="contact__line contact__line--web">www.pillarorchard.ca</p>
  </div>
</article>

</body>
</html>
```